Vesk Architecture

We are a architectural design and build company working between scales 1/1000 to 1/1 we want people to understand our difference from our design experience and quality.we build hotels restourants and office spaces.Our company name is Vesk architecture to mind sustainability.

We want to write our adress phone and work spesifications on the card and we want our logo as backround.

Ps:you could find the logo adress and phone box numbers from the web:www.veskmimarlik-ornek.com

Target Market(s)

Who looks for experts.

Industry/Entity Type

Architecture

Requirements
Must have
• Design is over everything.
Should not have
• we don want it to be colorfull

```html
<!DOCTYPE html>
<html lang="tr">
<head>
<meta charset="utf-8">
<title>Vesk Mimarlık – Kartvizit</title>
<link rel="stylesheet" href="https://fonts.googleapis.com/css2?family=Marcellus+SC&display=swap">
<style>
  :root {
    --teal: #2bbdb3;
    --paper: #ffffff;
    --ink: #111111;
    --page: #ffffff;
    --shadow: rgba(0, 0, 0, 0.28);
  }
  html, body {
    margin: 0;
    padding: 0;
    width: 1200px;
    height: 900px;
    overflow: hidden;
    background: var(--page);
  }
  .canvas {
    position: relative;
    width: 1200px;
    height: 900px;
  }
  .card {
    position: absolute;
    border-radius: 26px;
    overflow: hidden;
    box-shadow: 8px 10px 14px var(--shadow);
  }
  .card--front {
    left: 265px;
    top: 57px;
    width: 670px;
    height: 375px;
    background: var(--teal);
  }
  .card--back {
    left: 262px;
    top: 475px;
    width: 680px;
    height: 383px;
    background: var(--teal);
  }
  .card__face {
    position: absolute;
    inset: 0;
  }
  .wordmark {
    position: absolute;
    font-family: "Marcellus SC", serif;
    color: var(--ink);
    font-weight: 400;
    line-height: 1;
  }
  .wordmark__name {
    display: block;
    font-size: 82px;
    letter-spacing: 4px;
  }
  .wordmark__sub {
    display: block;
    font-size: 20px;
    letter-spacing: 3px;
    margin-top: 6px;
    margin-left: 3px;
  }
  .card--front .wordmark {
    left: 133px;
    top: 34px;
  }
  .card--back .wordmark {
    left: 233px;
    top: 110px;
  }
  .contact {
    position: absolute;
    left: 285px;
    top: 210px;
    margin: 0;
    font-family: "Marcellus SC", serif;
    font-size: 15px;
    line-height: 19.2px;
    color: var(--ink);
    font-style: normal;
    white-space: nowrap;
  }
  .contact span { display: block; }
</style>
</head>
<body>
<main class="canvas">
  <section class="card card--front" aria-label="Kartvizit ön yüz">
    <svg class="card__face" width="670" height="375" viewBox="0 0 670 375" aria-hidden="true">
      <path d="M55 0 Q25 187 55 375 L615 375 Q645 187 620 0 Z" fill="var(--paper)"/>
    </svg>
    <div class="wordmark">
      <span class="wordmark__name">Vesk</span>
      <span class="wordmark__sub">Mimarlık</span>
    </div>
    <address class="contact">
      <span>Deniz Arman KAYA - Mimar</span>
      <span>Ornek Mah. Liman Cad. Defne Sok.</span>
      <span>NO : 7 Kadikoy / ISTANBUL</span>
      <span>Tel&nbsp; : 0216 555 0142</span>
      <span>Fax :&nbsp; 0216 555 0187</span>
      <span>E-mail : veskmimarlik@ornekmail.com</span>
    </address>
  </section>

  <section class="card card--back" aria-label="Kartvizit arka yüz">
    <div class="wordmark">
      <span class="wordmark__name">Vesk</span>
      <span class="wordmark__sub">Mimarlık</span>
    </div>
  </section>
</main>
</body>
</html>
```